Land Buying Company Needs Letterhead for Direct Mail Marketing to Land Owners

We are looking for a professional letterhead that we will be including in our direct mail marketing. We will be sending this to land owners who may be interested in selling or purchasing land.

The letterhead needs to be editable. Headers and footers would look nice, but we are open. We would want it to include our address, website, phone, and email info. For right now the address to use for design purposes would the following:

Address: 417 Merriweather Avenue #300
Dallas, TX 75391
Website - www.quillbrookacres.example
Email - info@quillbrookacres.example
Phone - 866-420-ACRE

I have attached our logo zip file that we just had done on Pixel Bazaar. Let me know what questions you have, and thank you.

```html
<!DOCTYPE html>
<html lang="en">
<head>
<meta charset="utf-8">
<title>Quillbrook Acres Letterhead</title>
<link href="https://fonts.googleapis.com/css2?family=Montserrat:wght@300;400;500;700&display=swap" rel="stylesheet">
<style>
  :root {
    --backdrop: #f1f1f1;
    --paper: #e9eaea;
    --header-band: #d7dbd7;
    --forest: #465f2b;
    --lime: #8dc63f;
    --ink: #555a58;
    --ink-strong: #3b3f3d;
    --mark-faint: #dde0dd;
  }
  * { margin: 0; padding: 0; box-sizing: border-box; }
  html, body { width: 1200px; height: 795px; overflow: hidden; background: var(--backdrop); }
  body { font-family: "Montserrat", Arial, sans-serif; color: var(--ink); position: relative; }

  .letterhead {
    position: absolute; left: 333px; top: 20px;
    width: 534px; height: 755px;
    background: var(--paper);
    box-shadow: 0 6px 22px rgba(0,0,0,.18);
    overflow: hidden;
  }
  .header-band { position: absolute; left: 0; top: 0; width: 100%; height: 118px; background: var(--header-band); }

  .brand { position: absolute; left: 42px; top: 46px; display: flex; align-items: center; gap: 10px; }
  .brand-dot { width: 30px; height: 30px; border-radius: 50%; background: var(--forest); }
  .brand-name { font-weight: 700; font-size: 17px; letter-spacing: .5px; color: var(--lime); text-transform: uppercase; }

  .backdrop-mark {
    position: absolute; left: 200px; top: 190px; width: 290px; height: 290px;
    border-radius: 50%; background: var(--mark-faint);
  }

  .letter { position: absolute; left: 60px; top: 138px; width: 400px; font-weight: 400; font-size: 13px; line-height: 1.45; }
  .letter-date { margin-bottom: 6px; }
  .recipient { margin-bottom: 14px; }
  .salutation { font-weight: 700; color: var(--ink-strong); font-size: 15px; margin-bottom: 12px; }
  .letter-body { font-weight: 300; font-size: 14.5px; line-height: 1.5; color: #6a6f6d; position: relative; }
  .closing { margin-top: 34px; font-weight: 400; font-size: 15px; }
  .signature-area { width: 150px; height: 70px; margin-top: 8px; background: linear-gradient(90deg, rgba(60,60,60,.10), rgba(60,60,60,.03)); border-radius: 4px; }

  .company-address { position: absolute; right: 36px; top: 630px; text-align: right; font-size: 12.5px; line-height: 1.4; color: var(--ink-strong); }

  .footer-shape { position: absolute; left: 0; top: 0; width: 534px; height: 755px; }

  .contact-list { position: absolute; left: 44px; top: 680px; list-style: none; font-size: 11px; line-height: 1.55; color: #fff; }
  .contact-list li { display: flex; align-items: center; gap: 8px; }
  .contact-list svg { width: 11px; height: 11px; fill: #fff; }
</style>
</head>
<body>
  <main class="letterhead">
    <div class="header-band"></div>

    <div class="brand">
      <span class="brand-dot"></span>
      <span class="brand-name">Quillbrook Acres</span>
    </div>

    <div class="backdrop-mark"></div>

    <section class="letter">
      <p class="letter-date">Aug 16-2020</p>
      <p class="recipient">MR Jone doe<br>52 Larkmoor Ln<br>Fernhollow, NJ 08917</p>
      <p class="salutation">Dear Jone</p>
      <p class="letter-body">The standard chunk of Lorem Ipsum used since the 1500s is reproduced below for those interested. Sections 1.10.32 and 1.10.33 from "de Finibus Bonorum et Malorum" by Cicero are also reproduced in their exact original form, accompanied by English versions from the 1914 translation by H. Ashcombe.</p>
      <p class="closing">Yours faithfully</p>
      <div class="signature-area" role="img" aria-label="Handwritten signature"></div>
    </section>

    <svg class="footer-shape" viewBox="0 0 534 755" aria-hidden="true">
      <path d="M0,646 H262 C292,646 300,682 332,682 H534 V755 H0 Z" fill="var(--lime)"/>
      <path d="M0,656 H262 C292,656 300,692 332,692 H534 V755 H0 Z" fill="var(--forest)"/>
    </svg>

    <address class="company-address">417 Merriweather Avenue #300<br>Dallas, TX 75391</address>

    <ul class="contact-list">
      <li><svg viewBox="0 0 24 24"><path d="M6.6 10.8a15.1 15.1 0 0 0 6.6 6.6l2.2-2.2c.3-.3.7-.4 1-.2 1.1.4 2.3.6 3.6.6.6 0 1 .4 1 1V20c0 .6-.4 1-1 1A17 17 0 0 1 3 4c0-.6.4-1 1-1h3.5c.6 0 1 .4 1 1 0 1.3.2 2.5.6 3.6.1.3 0 .7-.2 1z"/></svg>866-420-ACRE</li>
      <li><svg viewBox="0 0 24 24"><path d="M2 5h20v14H2z M2 5l10 8 10-8" fill="none" stroke="#fff" stroke-width="2"/></svg>info@quillbrookacres.example</li>
      <li><svg viewBox="0 0 24 24"><circle cx="12" cy="12" r="9" fill="none" stroke="#fff" stroke-width="2"/><path d="M3 12h18M12 3c3 3 3 15 0 18M12 3c-3 3-3 15 0 18" fill="none" stroke="#fff" stroke-width="1.5"/></svg>www.quillbrookacres.example</li>
    </ul>
  </main>
</body>
</html>
```